Brightline Villas Estepona listings flyer

Brightline Villas Estepona are a specialist estate agency focussed solely on selling modern and contemporary homes.

We need an A4 folded flyer to be designed so that Brightline Villas Estepona can leaflet drop all of the modern homes for sale in our area to generate new instructions / listings. We need to engage with owners of those types of homes by posting this marketing material through their letter boxes in the hope that they see our funky and modern design and decide to call us about our services to sell their home, if for sale.

We would like to see sharp lines and a modern design (see our logo for style and colour scheme), with lots of white spaces and using photos which can blend in to the background to provide a powerful and impacting image to set us aside from any other direct mail leaflets which may be in their post box. It needs to show

* Quality
* Style
* Modern and forward thinking in design and outlook
* Professionalism

Front page
Top:
Logo of Brightline Villas Estepona.
Helping you sell your modern home. It’s all we do!

4 property photos in a grid position

Bottom banner
If you are thinking of selling, read on…

INSIDE LEFT & RIGHT (DOUBLE PAGE POSSIBLY BLANK WHITE BACKGROUND)
Title: Use Brightline Villas Estepona – the specialist modern homes agency to sell your home

We bring an exciting and dynamic mix of modern marketing with good old fashioned service to guarantee only the most qualified clients will be viewing your home (use online marketing image)

Marketing packages include stylish online brochures, professional photography, stunning drone video footage, informative video walk thru’s and unique floor plans (use drone and floor plan images)

Targeted social media campaigns focusing on international clientele actively looking to buy property in southern Spain (use social media image)

Bespoke, powerful advertising packages enable worldwide exposure for both online and traditional channels to market. We can be as discreet or as visible as you want us to be to sell your home

During our 20 years on the Costa del Sol, we have built up an enviable network of collaborating agents meaning you only have to instruct one expert real estate agent, Brightline Villas Estepona, to gain maximum exposure for your home

BACK PAGE

If you want service that matches the value of your home, contact us today for a private, personalised consultation. Brightline Villas Estepona. It’s all we do.

Suite 14
Torrenova Office Park
Calle Los Almendros
Valdemoro, Marbella

Tel: +34 952 418 306
Mobil y Whatsapp: +34 677 342 815
Email: info@brightlinevillasestepona.example
www.brightlinevillasestepona.example

Target Market(s)

Wealthy property owners of contemporary and modern homes who are looking to sell their home

Industry/Entity Type

Real Estate Agent

Font styles to use
Serif
Sans Serif

Colors
606060
e7e7e7
f5f5f5

Requirements
Must have
• Classy, professional, modern design with the ability to stand out from other leaflet drops / direct mail in letter box
Nice to have
• straight lines to border photos
• Maybe extend the lines further than they should so it has the look of an architects plan
• Blend in images to white background in the middle open double page
Should not have
• Lots of different colours

```html
<!DOCTYPE html>
<html lang="en">
<head>
<meta charset="utf-8">
<title>Brightline Villas Estepona – Flyer Front Page</title>
<link rel="stylesheet" href="https://fonts.googleapis.com/css2?family=Open+Sans:wght@400;600;700&display=swap">
<style>
  :root {
    --canvas-bg: #c4c3c8;
    --paper: #f5f5f5;
    --ink: #606060;
    --ink-soft: #8a8a8a;
    --line: #e7e7e7;
    --frame: #ffffff;
  }
  * { box-sizing: border-box; margin: 0; padding: 0; }
  html, body {
    width: 1200px;
    height: 900px;
    overflow: hidden;
  }
  body {
    background: var(--canvas-bg);
    font-family: "Open Sans", Arial, sans-serif;
    color: var(--ink);
    position: relative;
  }
  .flyer-front {
    position: absolute;
    left: 410px;
    top: 50px;
    width: 380px;
    height: 800px;
    background: var(--paper);
    box-shadow: 0 6px 24px rgba(0, 0, 0, 0.12);
    overflow: hidden;
  }
  .brand {
    position: absolute;
    top: 48px;
    right: 30px;
    display: flex;
    align-items: center;
    gap: 8px;
  }
  .brand-mark {
    width: 14px;
    height: 14px;
    background: var(--ink);
  }
  .brand-name {
    font-size: 12px;
    font-weight: 700;
    letter-spacing: 0.06em;
    text-transform: uppercase;
    color: var(--ink);
  }
  .photo-grid {
    position: absolute;
    left: 0;
    top: 0;
    width: 380px;
    height: 800px;
  }
  .photo-cell {
    stroke: var(--frame);
    stroke-width: 5;
  }
  .honeycomb-outline {
    fill: none;
    stroke: var(--line);
    stroke-width: 1.5;
  }
  .cta {
    position: absolute;
    right: 30px;
    bottom: 74px;
    text-align: right;
  }
  .cta-lead {
    font-size: 14px;
    font-weight: 400;
    color: var(--ink-soft);
  }
  .cta-main {
    font-size: 26px;
    font-weight: 700;
    color: var(--ink);
    line-height: 1.2;
  }
</style>
</head>
<body>
  <main class="flyer-front">
    <div class="brand">
      <span class="brand-mark"></span>
      <span class="brand-name">Brightline Villas Estepona</span>
    </div>

    <svg class="photo-grid" viewBox="0 0 380 800" xmlns="http://www.w3.org/2000/svg">
      <defs>
        <linearGradient id="tone-curved-villa" x1="0" y1="0" x2="0" y2="1">
          <stop offset="0" stop-color="#9fb8cf"/>
          <stop offset="0.45" stop-color="#8a5a3c"/>
          <stop offset="1" stop-color="#5b4a32"/>
        </linearGradient>
        <linearGradient id="tone-night-terrace" x1="0" y1="0" x2="1" y2="1">
          <stop offset="0" stop-color="#2e4a5c"/>
          <stop offset="0.6" stop-color="#5c7a7a"/>
          <stop offset="1" stop-color="#2a3c46"/>
        </linearGradient>
        <linearGradient id="tone-white-facade" x1="0" y1="0" x2="0" y2="1">
          <stop offset="0" stop-color="#4f78d0"/>
          <stop offset="0.45" stop-color="#e9ecef"/>
          <stop offset="1" stop-color="#22384c"/>
        </linearGradient>
        <linearGradient id="tone-pool-villa" x1="0" y1="0" x2="0" y2="1">
          <stop offset="0" stop-color="#3f8fd0"/>
          <stop offset="0.45" stop-color="#eef0ee"/>
          <stop offset="1" stop-color="#3fb5d8"/>
        </linearGradient>
      </defs>

      <polygon class="honeycomb-outline" points="4,230 57,138 163,138 216,230 163,322 57,322"/>
      <polygon class="honeycomb-outline" points="154,316.6 207,224.6 313,224.6 366,316.6 313,408.6 207,408.6"/>
      <polygon class="honeycomb-outline" points="154,489.8 207,397.8 313,397.8 366,489.8 313,581.8 207,581.8"/>

      <polygon class="photo-cell" fill="url(#tone-curved-villa)" role="img" aria-label="Photo of a curved modern villa with wide glazing at dusk"
        points="14,230 62,146.9 158,146.9 206,230 158,313.1 62,313.1"/>
      <polygon class="photo-cell" fill="url(#tone-night-terrace)" role="img" aria-label="Photo of a lit contemporary terrace at night"
        points="164,316.6 212,233.5 308,233.5 356,316.6 308,399.7 212,399.7"/>
      <polygon class="photo-cell" fill="url(#tone-white-facade)" role="img" aria-label="Photo of a white modern facade with glass balconies and a palm"
        points="14,403.2 62,320.1 158,320.1 206,403.2 158,486.3 62,486.3"/>
      <polygon class="photo-cell" fill="url(#tone-pool-villa)" role="img" aria-label="Photo of a white villa with a swimming pool and lawn"
        points="164,489.8 212,406.7 308,406.7 356,489.8 308,572.9 212,572.9"/>
    </svg>

    <div class="cta">
      <p class="cta-lead">If you are thinking of selling,</p>
      <p class="cta-main">Read on…</p>
    </div>
  </main>
</body>
</html>
```